Business cards for Brightmarrow Consulting with the following info for the front side:

Brightmarrow Consulting
Executive Coaching and Human Capital Strategy
www.brightmarrow.example

Lorena Vaduvic
Principal
lorena@brightmarrow.example
+1 604 555 0172

Black background, text using the colours of the logo - enclosed.

The back side of the business card should feature the logo in the middle, with "Executive Coaching and Human Capital Strategy" on top and "www.brightmarrow.example" below.

```html
<!DOCTYPE html>
<html lang="en">
<head>
<meta charset="utf-8">
<title>Brightmarrow Consulting – Business Cards</title>
<link rel="stylesheet" href="https://fonts.googleapis.com/css2?family=Montserrat:wght@400;500;700&display=swap">
<style>
  :root {
    --page: #e9e6e1;
    --card: #0d0e10;
    --blue: #2aa7e0;
    --yellow: #f5bd1f;
  }
  * { margin: 0; padding: 0; box-sizing: border-box; }
  html, body { width: 1200px; height: 909px; overflow: hidden; }
  body {
    background: var(--page);
    font-family: "Montserrat", sans-serif;
    position: relative;
  }
  .card {
    position: absolute;
    width: 560px;
    height: 320px;
    background: var(--card);
    border-radius: 22px;
    box-shadow: 0 12px 28px rgba(0,0,0,.35);
    overflow: hidden;
  }
  .card--back { left: 60px; top: 100px; }
  .card--front { left: 580px; top: 480px; }

  .brand {
    position: absolute;
    display: flex;
    align-items: center;
    gap: 14px;
  }
  .brand__dot {
    width: 64px; height: 64px;
    border-radius: 50%;
    border: 4px solid var(--yellow);
    flex: none;
  }
  .brand__name {
    font-weight: 500;
    font-size: 38px;
    letter-spacing: 1px;
    color: var(--blue);
    line-height: 1;
  }

  .tagline {
    position: absolute;
    color: var(--blue);
    font-size: 14px;
    letter-spacing: .4px;
    white-space: nowrap;
  }

  /* back side */
  .card--back .tagline { left: 0; right: 0; top: 62px; text-align: center; }
  .card--back .brand { left: 50%; top: 128px; transform: translateX(-50%); }
  .card--back .url {
    position: absolute; left: 0; right: 0; top: 238px;
    text-align: center; color: var(--yellow); font-size: 14px; letter-spacing: .4px;
  }

  /* front side */
  .card--front .brand { left: 56px; top: 58px; }
  .person {
    position: absolute; left: 40px; top: 168px; width: 236px; text-align: right;
  }
  .person__name { color: var(--yellow); font-weight: 700; font-size: 26px; line-height: 1.1; }
  .person__role { color: var(--blue); font-size: 15px; margin-top: 6px; }
  .divider {
    position: absolute; left: 296px; top: 150px; width: 1.5px; height: 92px;
    background: var(--yellow);
  }
  .contact { position: absolute; left: 316px; top: 148px; color: var(--blue); font-size: 12.5px; }
  .contact__company { font-weight: 500; font-size: 13.5px; letter-spacing: .5px; margin-bottom: 6px; }
  .contact__row { display: flex; align-items: center; gap: 7px; line-height: 1.75; }
  .contact__row svg { width: 11px; height: 11px; fill: var(--blue); flex: none; }
  .card--front .tagline { left: 0; right: 0; bottom: 30px; text-align: center; }
</style>
</head>
<body>

  <section class="card card--back" aria-label="Business card, back side">
    <p class="tagline">Executive Coaching and Human Capital Strategy</p>
    <div class="brand">
      <span class="brand__dot"></span>
      <span class="brand__name">BRIGHTMARROW</span>
    </div>
    <p class="url">www.brightmarrow.example</p>
  </section>

  <section class="card card--front" aria-label="Business card, front side">
    <div class="brand">
      <span class="brand__dot"></span>
      <span class="brand__name">BRIGHTMARROW</span>
    </div>

    <div class="person">
      <p class="person__name">Lorena Vaduvic</p>
      <p class="person__role">Principal</p>
    </div>

    <span class="divider"></span>

    <div class="contact">
      <p class="contact__company">BRIGHTMARROW CONSULTING</p>
      <p class="contact__row">
        <svg viewBox="0 0 24 24" aria-hidden="true"><path d="M6.6 10.8a15.1 15.1 0 0 0 6.6 6.6l2.2-2.2c.3-.3.7-.4 1-.2 1.1.4 2.3.6 3.6.6.6 0 1 .4 1 1V20c0 .6-.4 1-1 1A17 17 0 0 1 3 4c0-.6.4-1 1-1h3.5c.6 0 1 .4 1 1 0 1.3.2 2.5.6 3.6.1.3 0 .7-.2 1z"/></svg>
        +1 604 555 0172
      </p>
      <p class="contact__row">
        <svg viewBox="0 0 24 24" aria-hidden="true"><path d="M2 5h20v14H2z M3 6l9 7 9-7" fill="none" stroke="#2aa7e0" stroke-width="2"/></svg>
        lorena@brightmarrow.example
      </p>
      <p class="contact__row">
        <svg viewBox="0 0 24 24" aria-hidden="true"><circle cx="12" cy="12" r="9" fill="none" stroke="#2aa7e0" stroke-width="2"/><path d="M3 12h18M12 3c3 3 3 15 0 18M12 3c-3 3-3 15 0 18" fill="none" stroke="#2aa7e0" stroke-width="1.6"/></svg>
        www.brightmarrow.example
      </p>
    </div>

    <p class="tagline">Executive Coaching and Human Capital Strategy</p>
  </section>

</body>
</html>
```